Open Skye
A Bespoke Supported Living Service
Project: Open Skye
Industry: Disabilities
Open Skye - Disabilities
Creative Brief
I need double sided standard sized Business Card [3.5" x 2"]
Simple
Dorian Pluckett / Maud Finchley / Rosalind Obi
Director / Director / Manager
Gannet's Perch
42 Pelham Rd
Exmouth
Devon
Ex3 7qd
info@openskye-care.co.uk
www.openskye-care.co.uk
Hi Designers
i need 3 cards with the different names and contact details printed on each.
i will need cards, headed paper and compliment slips.
Thanks
Open Skye (logo)
Hi everyone.
Under the Open Skye logo Can you write the following; A Bespoke Supported Living Service
And the post code can you write it in block capitals ie, EX3 7QD
New link for logo

```html
<!DOCTYPE html>
<html lang="en">
<head>
<meta charset="utf-8">
<title>Open Skye – Stationery Set</title>
<link href="https://fonts.googleapis.com/css2?family=PT+Sans:wght@400;700&family=Great+Vibes&display=swap" rel="stylesheet">
<style>
  :root{
    --bg:#e8e5e0;
    --paper:#ffffff;
    --ink:#2a2a2a;
    --brand:#1b6fbf;
    --navy:#2b2d7f;
    --sky:#1aa3e0;
    --green:#3aa935;
    --orange:#f7a823;
    --yellow:#f5d22b;
    --rule:#3a3a3a;
  }
  *{box-sizing:border-box;margin:0;padding:0}
  html,body{width:1200px;height:479px;overflow:hidden}
  body{background:var(--bg);font-family:"PT Sans",sans-serif;color:var(--ink);position:relative}
  .sheet{position:absolute;background:var(--paper);overflow:hidden;box-shadow:0 1px 3px rgba(0,0,0,.18)}
  .wave{position:absolute;left:0;bottom:0;width:100%;display:block}
  .brand-name{font-family:"PT Sans",sans-serif;font-weight:700;color:var(--brand);line-height:1;white-space:nowrap}
  .tagline{color:#333;white-space:nowrap;line-height:1}

  /* letterhead */
  .letterhead{left:25px;top:31px;width:272px;height:352px}
  .letterhead .brand-name{position:absolute;left:91px;top:22px;font-size:21px}
  .letterhead .tagline{position:absolute;left:92px;top:47px;font-size:5.4px}
  .letterhead .wave{height:58px}
  .footer-address{position:absolute;right:27px;bottom:10px;font-size:4.2px;color:#fff;white-space:nowrap}
  .footer-contacts{position:absolute;left:26px;right:27px;bottom:3px;font-size:4.3px;color:#fff;display:flex;justify-content:space-between;white-space:nowrap}
  .footer-contacts b{font-weight:700}

  /* fax */
  .fax{left:326px;top:31px;width:271px;height:352px}
  .fax .brand-name{position:absolute;left:9px;top:23px;font-size:21px}
  .fax .tagline{position:absolute;left:10px;top:48px;font-size:5.4px}
  .contact-block{position:absolute;left:205px;top:10px;border-left:.5px solid #555;padding-left:5px;font-size:3.8px;line-height:1.3;height:40px;white-space:nowrap}
  .contact-block .gap{height:3px}
  .fax-title{position:absolute;left:11px;top:79px;font-size:19px;line-height:1;font-weight:400;letter-spacing:.2px}
  .fax-field{position:absolute;left:10px;width:250px;height:10px;border-bottom:.6px solid var(--rule);font-size:5px}
  .fax-field span{position:absolute;bottom:1px}
  .fax-field span+span{left:149px}
  .fax-options{position:absolute;left:10px;top:183px;width:252px;display:flex;justify-content:space-between;font-size:5px}
  .fax-options label{display:flex;align-items:center;gap:3px}
  .fax-options i{display:inline-block;width:6px;height:6px;border:.6px solid #333}
  .fax .wave{height:52px}

  /* envelope */
  .envelope{left:651px;top:32px;width:304px;height:136px}
  .envelope .flap{position:absolute;left:0;top:0;width:100%;height:55px}

  /* compliment slip */
  .compliment{left:627px;top:90px;width:303px;height:137px}
  .compliment .brand-name{position:absolute;left:9px;top:18px;font-size:20px}
  .compliment .tagline{position:absolute;left:10px;top:42px;font-size:4.8px}
  .compliment-script{position:absolute;left:8px;top:56px;font-family:"Great Vibes",cursive;font-size:18px;line-height:1.2;color:#222}
  .compliment .wave{height:60px}
  .compliment-footer{position:absolute;left:5px;bottom:2px;font-size:3.7px;color:#fff;white-space:nowrap}

  /* business cards */
  .card{position:absolute;width:112px;height:64px;background:var(--paper);border-radius:4px;overflow:hidden;box-shadow:0 1px 2px rgba(0,0,0,.2)}
  .card .brand-name{position:absolute;left:4px;top:18px;font-size:12px}
  .card .tagline{position:absolute;left:4px;top:35px;font-size:2.8px}
  .card .details{position:absolute;left:63px;top:9px;border-left:.4px solid #555;padding-left:4px;font-size:2.7px;line-height:1.3;white-space:nowrap}
  .card .details .gap{height:2px}
  .card .wave{height:24px}
  .card .person{position:absolute;right:6px;bottom:5px;font-size:3px;color:#fff;white-space:nowrap}
  .card .person b{font-weight:700}
  .card-1{left:646px;top:238px}
  .card-2{left:646px;top:310px}
  .card-3{left:646px;top:385px}

  .back-wave{left:841px;top:255px}
  .back-white{left:965px;top:255px}
  .back-blue{left:900px;top:334px;background:radial-gradient(ellipse at 50% 40%,#1f7fd6 0%,#1c4ea8 60%,var(--navy) 100%)}
  .back-card .brand-name{left:0;right:0;text-align:center}
  .back-card .tagline{left:0;right:0;text-align:center}
  .back-wave .brand-name{top:18px;font-size:13px}
  .back-wave .tagline{top:35px}
  .back-wave .url{position:absolute;right:8px;bottom:3px;font-size:3.2px;color:#fff}
  .back-white .brand-name{top:22px;font-size:13px}
  .back-white .tagline{top:38px}
  .back-white .url{position:absolute;left:0;right:0;top:47px;text-align:center;font-size:3.4px}
  .back-blue .brand-name{top:25px;font-size:13px;color:#fff}
  .back-blue .tagline{top:41px;color:#dce9ff}

  /* annotations */
  .note{position:absolute;font-size:7px;color:#333;white-space:nowrap}
  .note-cards{left:771px;top:334px}
  .note-back{left:1118px;top:321px}
  .connectors{position:absolute;left:0;top:0;width:1200px;height:479px;pointer-events:none}
</style>
</head>
<body>

<svg width="0" height="0" style="position:absolute">
  <defs>
    <linearGradient id="band" x1="0" x2="1" y1="0" y2="0">
      <stop offset="0" stop-color="#1aa3e0"/>
      <stop offset=".45" stop-color="#1c74c8"/>
      <stop offset="1" stop-color="#2b2d7f"/>
    </linearGradient>
    <linearGradient id="flapFill" x1="0" x2="1" y1="0" y2="0">
      <stop offset="0" stop-color="#1aa3e0"/>
      <stop offset="1" stop-color="#2b2d7f"/>
    </linearGradient>
  </defs>
</svg>

<!-- Letterhead -->
<section class="sheet letterhead" aria-label="Headed paper">
  <div class="brand-name">Open Skye</div>
  <div class="tagline">A Bespoke Supported Living Service</div>
  <svg class="wave" viewBox="0 0 600 120" preserveAspectRatio="none" aria-hidden="true">
    <path d="M0,45 C160,120 380,80 600,40 L600,120 L0,120 Z" fill="url(#band)"/>
    <path d="M0,28 C160,110 380,70 600,28" fill="none" stroke="#fff" stroke-width="8"/>
    <path d="M0,30 C160,112 380,72 600,30" fill="none" stroke="var(--orange)" stroke-width="5"/>
    <path d="M0,0 C140,85 380,50 600,10" fill="none" stroke="var(--green)" stroke-width="5"/>
  </svg>
  <div class="footer-address">Gannet's Perch 42 Pelham Rd, Exmouth Devon EX3 7QD</div>
  <div class="footer-contacts">
    <span>✆01632 960481</span><span>▯07700 900318</span><span>☎01632 960481</span><span>✉info@openskye-care.co.uk</span><span>www.<b>openskye-care</b>.co.uk</span>
  </div>
</section>

<!-- Fax sheet -->
<section class="sheet fax" aria-label="Fax sheet">
  <div class="brand-name">Open Skye</div>
  <div class="tagline">A Bespoke Supported Living Service</div>
  <div class="contact-block">
    <div>Gannet's Perch 42 Pelham Rd</div>
    <div>Exmouth Devon EX3 7QD</div>
    <div class="gap"></div>
    <div>✆ 01632 960481</div>
    <div>▯ 07700 900318</div>
    <div>☎ 01632 960481</div>
    <div>✉ info@openskye-care.co.uk</div>
    <div class="gap"></div>
    <div>www.<b>openskye-care</b>.co.uk</div>
  </div>
  <h1 class="fax-title">FAX</h1>
  <div class="fax-field" style="top:108px"><span>To :</span><span>From :</span></div>
  <div class="fax-field" style="top:124px"><span>Fax :</span><span>Pages :</span></div>
  <div class="fax-field" style="top:140px"><span>Phone :</span><span>Date :</span></div>
  <div class="fax-field" style="top:155px"><span>Re :</span><span>CC :</span></div>
  <div class="fax-options">
    <label><i></i>Urgent</label>
    <label><i></i>For Review</label>
    <label><i></i>Please Comment</label>
    <label><i></i>Please Reply</label>
    <label><i></i>Please Recycle</label>
  </div>
  <svg class="wave" viewBox="0 0 600 110" preserveAspectRatio="none" aria-hidden="true">
    <path d="M0,10 C80,120 360,100 600,45 L600,110 L0,110 Z" fill="url(#band)"/>
    <path d="M0,0 C80,112 360,92 600,36" fill="none" stroke="#fff" stroke-width="8"/>
    <path d="M0,2 C80,114 360,94 600,38" fill="none" stroke="var(--orange)" stroke-width="5"/>
    <path d="M0,-12 C70,100 360,80 600,22" fill="none" stroke="var(--green)" stroke-width="5"/>
  </svg>
</section>

<!-- Envelope -->
<section class="sheet envelope" aria-label="Envelope">
  <svg class="flap" viewBox="0 0 304 55" preserveAspectRatio="none" aria-hidden="true">
    <path d="M0,0 L304,0 L304,18 C300,30 290,32 250,36 L150,54 L40,34 C14,30 8,20 0,0 Z" fill="url(#flapFill)"/>
  </svg>
</section>

<!-- Compliment slip -->
<section class="sheet compliment" aria-label="Compliment slip">
  <div class="brand-name">Open Skye</div>
  <div class="tagline">A Bespoke Supported Living Service</div>
  <div class="compliment-script">With Compliments</div>
  <svg class="wave" viewBox="0 0 600 120" preserveAspectRatio="none" aria-hidden="true">
    <path d="M0,25 C60,115 360,100 600,45 L600,120 L0,120 Z" fill="url(#band)"/>
    <path d="M0,12 C60,105 360,88 600,35" fill="none" stroke="#fff" stroke-width="8"/>
    <path d="M0,14 C60,107 360,90 600,37" fill="none" stroke="var(--orange)" stroke-width="5"/>
    <path d="M0,0 C60,95 360,75 600,22" fill="none" stroke="var(--green)" stroke-width="5"/>
  </svg>
  <div class="compliment-footer">✆01632 960481 | ▯07700 900318 | ☎01632 960481 | ✉info@openskye-care.co.uk | www.<b>openskye-care</b>.co.uk | Gannet's Perch 42 Pelham Rd, Exmouth Devon EX3 7QD</div>
</section>

<!-- Business cards -->
<article class="card card-1" aria-label="Business card – Dorian Pluckett">
  <div class="brand-name">Open Skye</div>
  <div class="tagline">A Bespoke Supported Living Service</div>
  <div class="details">
    <div>Gannet's Perch 42 Pelham Rd</div><div>Exmouth Devon EX3 7QD</div><div class="gap"></div>
    <div>✆ 01632 960481</div><div>▯ 07700 900318</div><div>☎ 01632 960481</div><div>✉ info@openskye-care.co.uk</div><div class="gap"></div>
    <div>www.<b>openskye-care</b>.co.uk</div>
  </div>
  <svg class="wave" viewBox="0 0 240 50" preserveAspectRatio="none" aria-hidden="true">
    <path d="M0,12 C40,48 150,40 240,10 L240,50 L0,50 Z" fill="url(#band)"/>
    <path d="M0,7 C40,44 150,35 240,6" fill="none" stroke="var(--orange)" stroke-width="3"/>
    <path d="M0,0 C40,38 150,28 240,0" fill="none" stroke="var(--green)" stroke-width="2.5"/>
  </svg>
  <div class="person"><b>Dorian Pluckett</b> | Director</div>
</article>

<article class="card card-2" aria-label="Business card – Maud Finchley">
  <div class="brand-name">Open Skye</div>
  <div class="tagline">A Bespoke Supported Living Service</div>
  <div class="details">
    <div>Gannet's Perch 42 Pelham Rd</div><div>Exmouth Devon EX3 7QD</div><div class="gap"></div>
    <div>✆ 01632 960227</div><div>▯ 07700 900562</div><div>☎ 01632 960481</div><div>✉ info@openskye-care.co.uk</div>
    <div>www.<b>openskye-care</b>.co.uk</div>
  </div>
  <svg class="wave" viewBox="0 0 240 50" preserveAspectRatio="none" aria-hidden="true">
    <path d="M0,12 C40,48 150,40 240,10 L240,50 L0,50 Z" fill="url(#band)"/>
    <path d="M0,7 C40,44 150,35 240,6" fill="none" stroke="var(--orange)" stroke-width="3"/>
    <path d="M0,0 C40,38 150,28 240,0" fill="none" stroke="var(--green)" stroke-width="2.5"/>
  </svg>
  <div class="person"><b>Maud Finchley</b> | Director</div>
</article>

<article class="card card-3" aria-label="Business card – Rosalind Obi">
  <div class="brand-name">Open Skye</div>
  <div class="tagline">A Bespoke Supported Living Service</div>
  <div class="details">
    <div>Gannet's Perch 42 Pelham Rd</div><div>Exmouth Devon EX3 7QD</div><div class="gap"></div>
    <div>✆ 01632 960481</div><div>▯ 07700 900794</div><div>☎ 01632 960481</div><div>✉ info@openskye-care.co.uk</div>
    <div>www.<b>openskye-care</b>.co.uk</div>
  </div>
  <svg class="wave" viewBox="0 0 240 50" preserveAspectRatio="none" aria-hidden="true">
    <path d="M0,12 C40,48 150,40 240,10 L240,50 L0,50 Z" fill="url(#band)"/>
    <path d="M0,7 C40,44 150,35 240,6" fill="none" stroke="var(--orange)" stroke-width="3"/>
    <path d="M0,0 C40,38 150,28 240,0" fill="none" stroke="var(--green)" stroke-width="2.5"/>
  </svg>
  <div class="person"><b>Rosalind Obi</b> | Manager</div>
</article>

<!-- Back card options -->
<article class="card back-card back-wave" aria-label="Card back option with wave">
  <div class="brand-name">Open Skye</div>
  <div class="tagline">A Bespoke Supported Living Service</div>
  <svg class="wave" viewBox="0 0 240 50" preserveAspectRatio="none" aria-hidden="true">
    <path d="M0,12 C40,48 150,40 240,10 L240,50 L0,50 Z" fill="url(#band)"/>
    <path d="M0,7 C40,44 150,35 240,6" fill="none" stroke="var(--orange)" stroke-width="3"/>
    <path d="M0,0 C40,38 150,28 240,0" fill="none" stroke="var(--green)" stroke-width="2.5"/>
  </svg>
  <div class="url">www.<b>openskye-care</b>.co.uk</div>
</article>

<article class="card back-card back-white" aria-label="Card back option white">
  <div class="brand-name">Open Skye</div>
  <div class="tagline">A Bespoke Supported Living Service</div>
  <div class="url">www.<b>openskye-care</b>.co.uk</div>
</article>

<article class="card back-card back-blue" aria-label="Card back option blue">
  <div class="brand-name">Open Skye</div>
  <div class="tagline">A Bespoke Supported Living Service</div>
</article>

<!-- Annotations -->
<svg class="connectors" viewBox="0 0 1200 479" aria-hidden="true">
  <g fill="none" stroke="#555" stroke-width=".6">
    <path d="M760,259 H766 V422 H760"/>
    <path d="M766,338 H770"/>
    <path d="M1085,281 H1106 V373 H1018"/>
    <path d="M1106,325 H1116"/>
    <path d="M1089,278 L1085,281 L1089,284"/>
    <path d="M1022,370 L1018,373 L1022,376"/>
  </g>
</svg>
<div class="note note-cards">3 separate cards</div>
<div class="note note-back">Back Card _option</div>

</body>
</html>
```